Harbor of Kellvane - Lanternsdag Poster Design

We need a poster (8.5" x 11") for our Lanternsdag Celebration event June 18 - 19, 2016. I've included the Port logo, event logo, content, and some photos to choose from. Not all the photos have to be used, though. Feel free to use, crop and size photos how you see fit. Colors and fonts are also up to you. Looking for a fun design that screams family fun event!

Target Market(s)

Families

Industry/Entity Type

Event

Requirements
Must have
• The event logo, the Port logo, some photos (provided) and the content provided.

```html
<!DOCTYPE html>
<html lang="en">
<head>
<meta charset="utf-8">
<title>Lanternsdag Celebration Poster</title>
<link rel="stylesheet" href="https://fonts.googleapis.com/css2?family=Arvo:wght@700&family=Oswald:wght@600&family=Roboto+Condensed:wght@400;700&family=Jost:wght@400&display=swap">
<style>
  :root {
    --navy: #1d1f63;
    --red: #e0242b;
    --red-dark: #a8151b;
    --gold: #f2b33d;
    --white: #ffffff;
    --page: #e9e9ec;
    --ink: #1c1c2a;
  }
  * { margin: 0; padding: 0; box-sizing: border-box; }
  html, body { width: 1040px; height: 1200px; overflow: hidden; }
  body { background: var(--page); position: relative; font-family: "Jost", sans-serif; }

  .poster {
    position: absolute; left: 197px; top: 187px;
    width: 669px; height: 865px;
    background: linear-gradient(180deg, #dcdfe3 0%, #eceef1 45%, #e3e1e4 100%);
    overflow: hidden;
    box-shadow: 0 6px 18px rgba(0,0,0,.18);
  }
  .poster-backdrop { position: absolute; inset: 0; }
  .poster-art { position: absolute; left: 0; top: 0; width: 669px; height: 865px; }

  .event-mark {
    position: absolute; left: 268px; top: 222px; width: 200px;
    display: flex; flex-direction: column; align-items: center; gap: 8px;
    font-family: "Oswald", sans-serif; font-weight: 600;
    font-size: 26px; line-height: 1; color: var(--navy);
  }
  .event-mark .dot { width: 16px; height: 16px; border-radius: 50%; background: var(--red); }

  .banner-title {
    position: absolute; left: 0; width: 669px; top: 412px; text-align: center;
    font-family: "Oswald", sans-serif; font-weight: 600; font-size: 31px; line-height: 36px;
    color: var(--white); letter-spacing: .2px; white-space: nowrap;
  }
  .event-date {
    position: absolute; left: 0; width: 669px; top: 468px; text-align: center;
    font-family: "Arvo", serif; font-size: 37px; color: var(--navy); line-height: 40px;
  }
  .event-date .month { color: var(--red); }
  .event-venue {
    position: absolute; left: 0; width: 669px; top: 510px; text-align: center;
    font-family: "Arvo", serif; font-size: 27px; line-height: 32px; color: var(--navy);
  }
  .day-bar {
    position: absolute; left: 91px; width: 487px; height: 30px;
    background: var(--red); color: var(--white); text-align: center;
    font-family: "Roboto Condensed", sans-serif; font-weight: 700; font-size: 26px; line-height: 30px;
    box-shadow: 0 2px 3px rgba(0,0,0,.25);
  }
  .day-bar.first { top: 558px; }
  .day-bar.second { top: 741px; }

  .activity-col { position: absolute; top: 608px; }
  .activity-col h3 {
    font-family: "Roboto Condensed", sans-serif; font-weight: 700; font-size: 16.5px; line-height: 20px;
    color: var(--navy); margin-bottom: 6px; white-space: nowrap;
  }
  .activity-col ul { list-style: none; }
  .activity-col li {
    font-size: 14px; color: var(--ink); line-height: 20px; padding-left: 12px; position: relative; white-space: nowrap;
  }
  .activity-col li::before {
    content: ""; position: absolute; left: 0; top: 8px; width: 4px; height: 4px;
    border-radius: 50%; background: var(--red);
  }
  .col-family { left: 31px; }
  .col-family ul { margin-left: 34px; }
  .col-kids { left: 242px; }
  .col-norse { left: 393px; }
  .col-norse ul { margin-left: 18px; }

  .paddle-note {
    position: absolute; left: 0; width: 669px; top: 781px; text-align: center;
    font-size: 16px; color: var(--ink); line-height: 20px;
  }
  .info-footer {
    position: absolute; left: 0; bottom: 0; width: 669px; height: 34px;
    background: var(--navy); color: var(--white);
    font-family: "Roboto Condensed", sans-serif; font-size: 13.5px;
    display: flex; align-items: center; white-space: nowrap;
  }
  .info-footer .phone { width: 323px; padding-left: 26px; }
  .info-footer .web { padding-left: 13px; }
  .info-footer .or {
    width: 24px; height: 24px; border-radius: 50%; background: var(--white); flex: none;
    color: var(--red); font-weight: 700; font-size: 14px; text-align: center; line-height: 23px;
  }
</style>
</head>
<body>
  <main class="poster">
    <div class="poster-backdrop" role="img" aria-label="Faded photo of festival booths and visitors at the marina"></div>

    <svg class="poster-art" viewBox="0 0 669 865">
      <polygon points="0,0 356,0 356,330 253,318 0,310" fill="#6f7d5c" role="img" aria-label="Photo of a musician playing acoustic guitar outdoors"/>
      <polygon points="356,0 669,0 669,118 483,188 356,123" fill="#8a7d85" role="img" aria-label="Photo of dancers in traditional costume dancing in a circle"/>
      <polygon points="483,190 669,118 669,385 483,338" fill="#9ea3a6" role="img" aria-label="Photo of families at the fishing derby under a white tent"/>
      <polygon points="0,310 253,372 253,384 0,324" fill="var(--red)"/>
      <polygon points="483,338 669,385 669,397 483,350" fill="var(--red)"/>
      <polygon points="356,123 483,188 483,196 356,131" fill="var(--navy)"/>
      <polygon points="368,143 483,200 483,316 368,373 253,316 253,200" fill="var(--white)" stroke="var(--navy)" stroke-width="5"/>
      <polygon points="35,412 105,398 92,432 112,462 48,468 70,440" fill="var(--red-dark)"/>
      <polygon points="634,412 564,398 577,432 557,462 621,468 599,440" fill="var(--red-dark)"/>
      <path d="M95,402 Q334,380 574,402 L574,456 Q334,434 95,462 Z" fill="var(--red)" stroke="var(--gold)" stroke-width="3"/>
    </svg>

    <div class="event-mark"><span class="dot"></span>Lanternsdag</div>

    <h1 class="banner-title">Lanternsdag Celebration</h1>
    <p class="event-date"><span class="month">June</span> 18 -19</p>
    <p class="event-venue">At the Kellvane Marina</p>

    <h2 class="day-bar first">On June 18th</h2>

    <section class="activity-col col-family">
      <h3>Fun For The Whole Family:</h3>
      <ul><li>2-for-1 Moorage</li><li>Live Music</li><li>Hot Dog Vendor</li><li>Boating Squadron</li></ul>
    </section>
    <section class="activity-col col-kids">
      <h3>Kid’s Activities:</h3>
      <ul><li>Fishing Derby</li><li>Touch a Fire Truck</li><li>Toy Boat Building</li></ul>
    </section>
    <section class="activity-col col-norse">
      <h3>Traditional Norwegian Activities:</h3>
      <ul><li>Raising the Mai “Green” Stang</li><li>Traditional Norwegian Food<br>and Dancing</li><li>Bonfire Lighting with the<br>Kellvane Vikings</li></ul>
    </section>

    <h2 class="day-bar second">On June 19th</h2>
    <p class="paddle-note">Brisk Sound Water Trails Festival – Coves to Keldport Fun Paddle<br>A fun event for paddlers of all levels!</p>

    <footer class="info-footer">
      <span class="phone">For more information, please call (555) 014-2290 ext. 1</span>
      <span class="or">or</span>
      <span class="web">On the web at www.harborofkellvane.com/lanternsdag-2</span>
    </footer>
  </main>
</body>
</html>
```